Mail order Nursery needs banner for promoting perennials that compliment roses.

banner should be 1135 wide x165 tall. We have an existing one displayed but we are not happy with the way it is washed out. Use your creativity to give us something that pops. Would love to see some watercolor or some other form of image other than just words washed across a stock photo. Banner needs to read Perennial Companions for Roses or some variation of that. Colors need to compliment our current theme. You can view the page and banner I want to replace at www.meadowlarkbloomyard.com. The banner we want to replace has been uploaded to the pixel forum file drop box. Thanks for your help and I look forward to seeing what you guys come up with. EDIT: I don't think I was clear enough in by brief. This banner promotes the sale of plants that look good planted with roses. We are getting to many submissions that are using only roses as the backdrop. We are looking for different types of plants that you would grow in your garden to compliment your roses. Thanks for all your hard work.

Target Market(s)

Home owners between 30 and 65

Industry/Entity Type

Nursery

Colors
33a6d7
e667a6

Requirements
Must have
• Text promotion perennials that compliment roses.... does not have to be those exact words but get the point across
Should not have
• Stock Photos with simple text washed across it.

```html
<!DOCTYPE html>
<html lang="en">
<head>
<meta charset="utf-8">
<title>Perennial Companions for Roses</title>
<link href="https://fonts.googleapis.com/css2?family=Marcellus&family=Great+Vibes&display=swap" rel="stylesheet">
<style>
  :root {
    --sky: #33a6d7;
    --rose: #e667a6;
    --paper: #f1e8d8;
    --paper-shade: #e2d3bb;
    --paper-edge: #c9b392;
    --bloom-magenta: #c0359a;
    --bloom-pink: #e7699f;
    --bloom-violet: #8a4bb0;
    --leaf: #3f6b2c;
    --leaf-dark: #24401a;
    --salvia: #5a62b8;
  }
  html, body {
    margin: 0;
    padding: 0;
    overflow: hidden;
    background: #ffffff;
  }
  .banner {
    position: relative;
    width: 1200px;
    height: 174px;
    overflow: hidden;
  }
  .garden-scene {
    position: absolute;
    inset: 0;
    background:
      radial-gradient(ellipse 220px 90px at 640px 140px, var(--bloom-magenta) 0%, transparent 70%),
      radial-gradient(ellipse 260px 100px at 880px 130px, var(--bloom-pink) 0%, transparent 72%),
      radial-gradient(ellipse 200px 80px at 1110px 120px, #dd4b6a 0%, transparent 70%),
      radial-gradient(ellipse 260px 70px at 900px 30px, #d9d9e8 0%, transparent 70%),
      radial-gradient(ellipse 200px 60px at 1120px 20px, var(--salvia) 0%, transparent 70%),
      radial-gradient(ellipse 180px 60px at 620px 40px, var(--leaf) 0%, transparent 75%),
      linear-gradient(180deg, #5b7a4a 0%, var(--leaf) 40%, var(--bloom-violet) 100%);
  }
  .paper-panel {
    position: absolute;
    left: 0;
    top: 0;
    width: 545px;
    height: 174px;
  }
  .headline {
    position: absolute;
    left: 0;
    top: 0;
    width: 540px;
    height: 174px;
    margin: 0;
    font-weight: normal;
  }
  .headline-perennial {
    position: absolute;
    left: 60px;
    top: 12px;
    font-family: "Marcellus", serif;
    font-size: 81px;
    line-height: 1;
    letter-spacing: 1px;
    color: var(--sky);
  }
  .headline-companions {
    position: absolute;
    left: 44px;
    top: 78px;
    font-family: "Great Vibes", cursive;
    font-size: 64px;
    line-height: 1;
    color: var(--rose);
  }
  .headline-for {
    position: absolute;
    left: 305px;
    top: 112px;
    font-family: "Marcellus", serif;
    font-size: 22px;
    line-height: 1;
    color: var(--sky);
  }
  .headline-roses {
    position: absolute;
    left: 358px;
    top: 92px;
    font-family: "Marcellus", serif;
    font-size: 47px;
    line-height: 1;
    color: var(--rose);
  }
</style>
</head>
<body>
  <div class="banner">
    <div class="garden-scene" role="img" aria-label="Garden bed of pink and purple petunias with blue and white salvia spikes behind"></div>

    <svg class="paper-panel" width="545" height="174" viewBox="0 0 545 174" aria-hidden="true">
      <defs>
        <linearGradient id="paper-fill" x1="0" y1="0" x2="1" y2="0">
          <stop offset="0" stop-color="var(--paper-shade)"/>
          <stop offset="0.08" stop-color="var(--paper)"/>
          <stop offset="0.9" stop-color="var(--paper)"/>
          <stop offset="1" stop-color="var(--paper-shade)"/>
        </linearGradient>
      </defs>
      <path d="M0 0 H512 L516 10 L509 22 L518 34 L512 47 L521 60 L514 74 L523 88 L516 101 L526 114 L519 128 L528 141 L522 154 L531 166 L527 174 H0 Z"
            fill="var(--paper-edge)"/>
      <path d="M0 0 H506 L510 10 L503 22 L512 34 L506 47 L515 60 L508 74 L517 88 L510 101 L520 114 L513 128 L522 141 L516 154 L525 166 L521 174 H0 Z"
            fill="url(#paper-fill)"/>
    </svg>

    <h1 class="headline">
      <span class="headline-perennial">PERENNIAL</span>
      <span class="headline-companions">Companions</span>
      <span class="headline-for">FOR</span>
      <span class="headline-roses">ROSES</span>
    </h1>
  </div>
</body>
</html>
```